Business card design needed

Family General Practitioner/ Family Physician.
Logo is the logo of the Imperial Guild of Community Clinicians Oceania
http://pkvtm.lorimar.example/PictureGallery/logos/pages/IGCCO%20logo_jpg.htm

Reason: Just a bit more time to make changes and the weekend for me to look at things closely and to choose. Thanks, Ulan

Thanks for all the submissions. So many of them are really works of art. Not one of them are not good. The ones that I am eliminating are the ones that I think are not suitable for me personally only, and because if I don't, it makes it very difficult to decide as many of you are also sending me slight variations of a card. I have just decided to choose a second place card too. Can't thank you all enough. Good luck, Ulan. P.S - Working today till 10 pm as the card says :-), so probably won't be able to give a feedback till late Saturday night or Sunday morning here in Sydney, Australia. 

Reason: Just added a second place to the budget and realised that Australia is ahead of the rest of the world in the time zone (only :-) - don't want to offend anyone or start a debate!! ) , so Monday deadline will mean it will be a weekend for the rest of the world. Just wanted to give everyone more time to submit their best, especially since I will be picking a second card too. Can't thank everyone enough for the submissions. P.S - Not keen on photos on the card.

Business

Contact Information for Business Card

Dr. Ulan Pereira M.B.B.S., F.I.G.C.C.O
Family General Practitioner
Address, timings, phone and fax number on the back.

Requirements
Must have
• Timings
Mon 7 am - 7 pm
Tues 7 am - 12 pm
Wed 7 am - 10 pm
Thurs 7 am - 12 pm
Fri 7 am - 8 pm
Sat 8 am - 10 pm
Sun - Off

```html
<!DOCTYPE html>
<html lang="en">
<head>
<meta charset="utf-8">
<title>Dr. Ulan Pereira – Business Card</title>
<link rel="stylesheet" href="https://fonts.googleapis.com/css2?family=Source+Sans+3:ital,wght@0,400;0,600;0,700;1,400;1,600&display=swap">
<style>
  :root {
    --page-bg: #d9d9d9;
    --card-white: #ffffff;
    --blue: #1f62b0;
    --blue-light: #2f78c8;
    --blue-dark: #164e8e;
    --blue-text: #1f5ba8;
    --white: #ffffff;
  }
  * { box-sizing: border-box; margin: 0; padding: 0; }
  html, body {
    width: 1200px; height: 848px; overflow: hidden;
    background: var(--page-bg);
    font-family: "Source Sans 3", sans-serif;
  }
  .canvas { position: relative; width: 1200px; height: 848px; }
  .card {
    position: absolute; width: 520px; height: 318px;
    background: var(--card-white); overflow: hidden;
    box-shadow: 0 6px 18px rgba(0,0,0,0.25);
  }
  .card-front { left: 90px; top: 90px; }
  .card-back { left: 590px; top: 440px; }

  .front-shapes { position: absolute; inset: 0; }
  .guild-mark {
    position: absolute; right: 34px; top: 36px;
    display: flex; align-items: center; gap: 8px;
    color: var(--blue-text); font-weight: 700; font-size: 22px; letter-spacing: 0.04em;
  }
  .guild-mark .dot { width: 18px; height: 18px; border-radius: 50%; background: var(--blue-text); }
  .doctor { position: absolute; left: 30px; top: 120px; color: var(--white); }
  .doctor-name { font-size: 27px; font-weight: 700; line-height: 1.1; }
  .credentials { margin-top: 6px; margin-left: 6px; font-size: 15px; font-weight: 400; letter-spacing: 0.02em; }
  .role { margin-left: 4px; font-size: 16px; font-style: italic; }
  .tagline { position: absolute; left: 36px; top: 228px; color: var(--white); font-size: 20px; font-style: italic; }

  .hours {
    position: absolute; left: 0; right: 0; top: 30px;
    text-align: center; color: var(--blue-text);
    font-size: 21px; font-style: italic; line-height: 40px;
  }
  .contact-band {
    position: absolute; left: 0; right: 0; bottom: 0; height: 122px;
    background: var(--blue); color: var(--white); text-align: center;
    padding-top: 14px;
  }
  .address { font-size: 15px; font-style: italic; line-height: 20px; }
  .numbers { margin-top: 8px; font-size: 18px; }
  .numbers .phone { font-weight: 700; }
</style>
</head>
<body>
<main class="canvas">
  <section class="card card-front" aria-label="Card front">
    <svg class="front-shapes" width="520" height="318" viewBox="0 0 520 318" aria-hidden="true">
      <defs>
        <linearGradient id="frontBlue" x1="0" y1="0" x2="1" y2="1">
          <stop offset="0" stop-color="#1a5aa6"/>
          <stop offset="1" stop-color="#2d74c4"/>
        </linearGradient>
      </defs>
      <path d="M0,0 H170 C250,150 390,240 520,262 V318 H0 Z" fill="url(#frontBlue)"/>
      <path d="M0,0 H90 C170,120 330,230 520,290 V318 H0 Z" fill="#1d60ad" opacity="0.55"/>
      <path d="M0,182 L420,318 H0 Z" fill="#154b88" opacity="0.75"/>
    </svg>
    <div class="guild-mark"><span class="dot"></span>IGCCO</div>
    <div class="doctor">
      <h1 class="doctor-name">Dr. Ulan Pereira</h1>
      <p class="credentials">M.B.B.S., F.I.G.C.C.O</p>
      <p class="role">Family General Practitioner</p>
    </div>
    <p class="tagline">"Caring about your health"</p>
  </section>

  <section class="card card-back" aria-label="Card back">
    <div class="hours">
      <p>Mon 7am - 7pm • Tues 7am - 12pm</p>
      <p>Wed 7am - 10pm • Thurs 7am - 12pm</p>
      <p>Fri 7am - 8pm • Sat 8am - 10pm</p>
    </div>
    <div class="contact-band">
      <p class="address">Level 2, Orchard Arcade, Kestrel Park Shopping Centre<br>Fernvale, NSW 2199</p>
      <p class="numbers"><span class="phone">P: 02 5550 1400</span> • <span class="fax">F: 02 5550 1433</span></p>
    </div>
  </section>
</main>
</body>
</html>
```